当社は、神戸で埋蔵文化財発掘調査を行う会社として営業しております。
この業界では、全国的に有名ではあるのですが、この度、新たな顧客獲得の一つのアイテムとしてDMを検討しております。
一般的にそんな仕事が存在している事の認識が低く、シンプルでインパクトの強いDMのデザインの作成をお願いします。

①DMデザインの作成(B5サイズ)
②表面 当社ロゴ、住所、TEL、FAX、URL
③裏面 シンプルでインパクトのあるもの

埋蔵文化財発掘調査について詳しく無い方も沢山おられると思いますので、
当社HP http://www.tamurakensa.com/ で確認してください。

イラストレーター形式
PDF形式
質疑回答を元に、裏面を尚且つシンプルで埋蔵文化財発掘調査をインパクトあるデザインをお願いします。
尚、ハガキとして郵送の予定です。

シンプルかつインパクトのあるデザインで、受け取り手にも会社の内容が伝わりやすいと思い採用させて頂きました。

たくさんのご提案頂きまして、誠にありがとうございます。
選考中も非常に悩むデザインが多く、選考に時間が掛かってしまいました。
本当にありがとうございました。

```html
<!DOCTYPE html>
<html lang="ja">
<head>
<meta charset="utf-8">
<title>埋蔵文化財発掘調査業務</title>
<link href="https://fonts.googleapis.com/css2?family=Noto+Sans+JP:wght@400;500;700;900&family=Roboto:wght@500;700&display=swap" rel="stylesheet">
<style>
  :root {
    --teal: #1f8f78;
    --teal-dark: #15705d;
    --teal-light: #d7ece6;
    --paper: #f4f5f4;
    --ink: #2d3432;
    --white: #ffffff;
  }
  * { box-sizing: border-box; margin: 0; padding: 0; }
  html, body { width: 851px; height: 1200px; overflow: hidden; background: var(--white); }
  body { font-family: "Noto Sans JP", sans-serif; color: var(--ink); position: relative; }

  .upper { position: absolute; left: 0; top: 0; width: 851px; height: 830px; background: linear-gradient(#ffffff, var(--paper)); }

  .headline { position: absolute; top: 510px; left: 0; width: 100%; text-align: center; }
  .headline .eyebrow { font-family: "Roboto", sans-serif; font-weight: 700; color: var(--teal); font-size: 19px; letter-spacing: 2px; }
  .headline h1 { font-weight: 900; font-size: 56px; letter-spacing: 3px; color: var(--ink); margin-top: 4px; line-height: 1.2; }

  .intro { position: absolute; top: 640px; left: 40px; width: 771px; font-size: 14.5px; line-height: 1.75; color: var(--ink); }

  .artifact { position: absolute; left: 380px; top: 738px; width: 92px; height: 150px; border-radius: 46px 46px 14px 14px; background: linear-gradient(#3aa58d, var(--teal-dark)); z-index: 2; }

  .process { position: absolute; left: 0; top: 826px; width: 851px; height: 234px; background: var(--teal); }
  .process-grid { position: absolute; left: 34px; top: 86px; width: 784px; display: grid; grid-template-columns: repeat(4, 178px); column-gap: 24px; row-gap: 22px; }
  .step { position: relative; height: 48px; background: var(--white); color: var(--teal-dark); font-weight: 700; font-size: 19px; display: flex; align-items: center; justify-content: center; letter-spacing: 1px; }
  .step.label { background: var(--teal-dark); color: var(--white); font-family: "Roboto", sans-serif; font-size: 18px; }
  .step:not(:nth-child(4n))::after { content: ""; position: absolute; right: -17px; top: 17px; border-left: 10px solid var(--white); border-top: 7px solid transparent; border-bottom: 7px solid transparent; }

  .footer { position: absolute; left: 0; top: 1060px; width: 851px; height: 140px; background: var(--white); }
  .company { position: absolute; left: 36px; top: 26px; }
  .company .services { font-size: 11px; color: var(--ink); margin-left: 40px; }
  .company .brand { display: flex; align-items: center; gap: 10px; margin-top: 2px; }
  .company .mark { width: 30px; height: 30px; border-radius: 50%; background: var(--teal); }
  .company .name { font-size: 28px; font-weight: 500; color: var(--ink); letter-spacing: 1px; }
  .company .address { font-size: 12px; margin-top: 10px; }

  .contact { position: absolute; right: 34px; top: 22px; text-align: right; }
  .contact .tel { font-family: "Roboto", sans-serif; font-weight: 700; font-size: 44px; color: var(--teal); letter-spacing: 1px; }
  .contact .sub { font-family: "Roboto", sans-serif; font-weight: 500; font-size: 16px; color: var(--teal); margin-top: 8px; }
</style>
</head>
<body>
  <div class="upper"></div>

  <header class="headline">
    <p class="eyebrow">EXCAVATION</p>
    <h1>埋蔵文化財発掘調査業務</h1>
  </header>

  <p class="intro">文化財保護法に基づき建設工事を行うにあたり、埋蔵文化財の試掘調査・発掘調査の必要が生じてまいります。<br>弊社は多くの実績を持ち全国においてご対応可能です。些細なことからでもお気軽にご相談ください。</p>

  <div class="artifact" role="img" aria-label="埴輪のイラスト"></div>

  <section class="process">
    <div class="process-grid">
      <div class="step label">PROCESS</div>
      <div class="step">ご相談・確認</div>
      <div class="step">発掘・測量</div>
      <div class="step">遺物洗浄</div>
      <div class="step">説明会開催</div>
      <div class="step">復元作業</div>
      <div class="step">実測・図化</div>
      <div class="step">報告書作成</div>
    </div>
  </section>

  <footer class="footer">
    <div class="company">
      <p class="services">埋蔵文化財発掘調査業務・土木工事・建築工事</p>
      <div class="brand"><span class="mark"></span><span class="name">田村建査工業株式会社</span></div>
      <p class="address">〒650-0000 兵庫県神戸市西区みどり台1丁目2番3号</p>
    </div>
    <div class="contact">
      <p class="tel">TEL.078-555-0142</p>
      <p class="sub">FAX.078-555-0148 www.tamurakensa.com</p>
    </div>
  </footer>
</body>
</html>
```